Spring Anti-wrinkle Injections Poster

A1 size poster for Spring promoting anti-wrinkle injections (Velarix)
Poster is to promote rejuvination and refreshing of the appreaance coming into the warmer months.

Please feel free to add promotional message. We want to encourage walk by traffic to have anti-wrinkle treatments.

- Poster must not be overly feminine.
- Promote Velarix injections for smoothing and refreshing apprearance (word
velarix can not be used please use 'Anti-wrinkle injection')

Industry/Entity Type

Promotional

Requirements
Must have
• - Logo (attached)

- 4 clinic locations with contact numbers
Suite 305, 48 Farrow Street, Melbourne 9217 4083
587 Bradwell Street, Richmond 9316 7541
Shop 9 Pelling Arcade, Dandenong 9582 6139
17 Drayford Walk, Mount Waverley 9671 3054

- Website
www.lumadorvale.com

- Feel and look of poster to be targeted towards females but not overly feminine, we are a unisex clinic.
Should not have
• - The word velarix can not be used please use 'Anti-wrinkle injection' instead

```html
<!DOCTYPE html>
<html lang="en">
<head>
<meta charset="utf-8">
<title>Anti-wrinkle Injection – Spring Poster</title>
<link rel="stylesheet" href="https://fonts.googleapis.com/css2?family=Didact+Gothic&display=swap">
<style>
  :root {
    --paper-light: #fdf1e7;
    --paper-mid: #f7dfcc;
    --paper-shadow: #efcdb5;
    --paper-deep: #e8c2a6;
    --ink: #111111;
    --brand-violet: #a365b4;
  }
  html, body {
    margin: 0;
    padding: 0;
    width: 848px;
    height: 1200px;
    overflow: hidden;
    background: #ffffff;
  }
  .poster {
    position: relative;
    width: 848px;
    height: 1200px;
    overflow: hidden;
    font-family: "Didact Gothic", "Century Gothic", sans-serif;
    color: var(--ink);
  }
  .paper-texture {
    position: absolute;
    inset: 0;
    background:
      radial-gradient(ellipse 45% 30% at 78% 22%, var(--paper-light) 0%, transparent 100%),
      radial-gradient(ellipse 40% 25% at 30% 30%, rgba(232, 194, 166, 0.45) 0%, transparent 100%),
      radial-gradient(ellipse 35% 22% at 70% 60%, rgba(253, 241, 231, 0.8) 0%, transparent 100%),
      radial-gradient(ellipse 45% 30% at 25% 70%, rgba(232, 194, 166, 0.55) 0%, transparent 100%),
      radial-gradient(ellipse 40% 25% at 60% 90%, rgba(239, 205, 181, 0.7) 0%, transparent 100%),
      linear-gradient(160deg, var(--paper-light) 0%, var(--paper-mid) 50%, var(--paper-shadow) 100%);
  }
  .brand-name {
    position: absolute;
    top: 88px;
    right: 15px;
    margin: 0;
    font-size: 25px;
    line-height: 30px;
    font-weight: 400;
    color: var(--brand-violet);
    letter-spacing: 1px;
  }
  .headline {
    position: absolute;
    top: 542px;
    left: 0;
    width: 100%;
    margin: 0;
    text-align: center;
    font-size: 63px;
    line-height: 76px;
    font-weight: 400;
    letter-spacing: 0.5px;
  }
  .contact {
    position: absolute;
    left: 14px;
    bottom: 1px;
  }
  .contact-website {
    margin: 0 0 -2px;
    font-size: 31px;
    line-height: 36px;
    letter-spacing: 1px;
  }
  .clinic-list {
    list-style: none;
    margin: 0;
    padding: 0;
    font-size: 19.5px;
    line-height: 28px;
    letter-spacing: 0.7px;
  }
</style>
</head>
<body>
  <main class="poster">
    <div class="paper-texture" role="img" aria-label="Crumpled peach paper texture filling the background"></div>

    <p class="brand-name">Lumador Vale Clinic</p>

    <h1 class="headline">anti-wrinkle injection</h1>

    <footer class="contact">
      <p class="contact-website">www.lumadorvale.com</p>
      <ul class="clinic-list">
        <li>-Suite 305, 48 Farrow Street, Melbourne 9217 4083</li>
        <li>-587 Bradwell Street, Richmond 9316 7541</li>
        <li>-Shop 9 Pelling Arcade, Dandenong 9582 6139</li>
        <li>-17 Drayford Walk, Mount Waverley 9671 3054</li>
      </ul>
    </footer>
  </main>
</body>
</html>
```